Composite decking sales poster

Poster advertising our brand of decking and our industry-best warranty.
Poster dimensions 1200mm wide x 400mm high.
50 Year Stain and Fade Warranty.
Ultra-Low Maintenance.
Environmentally Friendly Made from Recycled Materials.
Website: https://brimlaydecking.com.au
Phone: 1300 947 325
*** Uploaded pictures are optional to use ***
Must list website, phone number and logos.

```html
<!DOCTYPE html>
<html lang="en">
<head>
<meta charset="utf-8">
<title>Brimlay Composites – Decking Poster</title>
<link rel="stylesheet" href="https://fonts.googleapis.com/css2?family=Montserrat:ital,wght@0,500;0,600;0,700;1,700;1,900&family=Open+Sans:wght@400;600;700&display=swap">
<style>
  :root{
    --surround:#d6d6d6;
    --white:#ffffff;
    --ink:#3a3a3a;
    --navy:#1f2b45;
    --brand-blue:#2e6db4;
    --band-grey:#8e8880;
    --deck-light:#b9a9a3;
    --deck-mid:#7a6560;
    --deck-dark:#4e3f3d;
    --bar-dark:#3b3b3b;
    --badge:#6f6862;
    --frame:#d9d6d6;
  }
  *{box-sizing:border-box;margin:0;padding:0}
  html,body{width:1200px;height:456px;overflow:hidden;background:var(--surround)}
  .poster{
    position:absolute;left:53px;top:45px;width:1095px;height:366px;overflow:hidden;
    box-shadow:0 3px 8px rgba(0,0,0,.35);
  }
  .deck-photo{
    position:absolute;inset:0;
    background:
      radial-gradient(ellipse at 5% 20%, rgba(230,220,200,.75), rgba(230,220,200,0) 35%),
      linear-gradient(160deg,var(--deck-light) 0%,var(--deck-mid) 40%,var(--deck-dark) 100%);
  }
  .header-curve{position:absolute;left:0;top:0;width:1095px;height:130px}
  .brand{position:absolute;left:38px;top:16px;display:flex;align-items:center;gap:12px}
  .brand-mark{width:34px;height:34px;background:var(--brand-blue)}
  .brand-name{font:700 30px/1 "Montserrat",sans-serif;color:var(--ink);letter-spacing:-.5px}
  .website{position:absolute;left:122px;top:70px;font:italic 700 14.5px/1 "Montserrat",sans-serif;color:var(--ink)}
  .inset-frame{
    position:absolute;left:24px;top:153px;width:348px;height:185px;
    background:var(--frame);border-radius:0 38px 0 0;padding:5px;
  }
  .inset-photo{
    width:100%;height:100%;border-radius:0 34px 0 0;
    background:linear-gradient(110deg,#6b4a2e 0%,#b07a4a 30%,#8c7a6a 55%,#c9b7a3 75%,#7d8a6a 100%);
  }
  .headline{
    position:absolute;left:424px;top:72px;white-space:nowrap;
    font:italic 900 44px/41px "Montserrat",sans-serif;color:var(--white);
    text-shadow:3px 3px 0 var(--navy);letter-spacing:-.8px;
  }
  .feature-icon{position:absolute;top:210px;width:72px;height:71px;background:var(--white);border-radius:8px;display:flex;align-items:center;justify-content:center}
  .feature-icon svg{width:52px;height:52px}
  .icon-maintenance{left:431px}
  .icon-eco{left:640px}
  .feature-label{position:absolute;font:600 15px/20px "Montserrat",sans-serif;color:var(--white);white-space:nowrap}
  .label-maintenance{left:408px;top:293px;width:126px;text-align:center;letter-spacing:.3px}
  .label-eco{left:579px;top:293px;letter-spacing:.3px}
  .divider{position:absolute;left:554px;top:297px;width:2px;height:34px;background:var(--white)}
  .phone-bar{position:absolute;left:840px;top:188px;width:255px;height:33px;background:var(--bar-dark)}
  .phone-icon{position:absolute;left:835px;top:183px;width:43px;height:43px;border-radius:50%;background:var(--white);border:3px solid var(--bar-dark);display:flex;align-items:center;justify-content:center}
  .phone-number{position:absolute;left:888px;top:188px;font:600 27px/33px "Open Sans",sans-serif;color:var(--white);letter-spacing:1.5px;white-space:nowrap}
  .badge{
    position:absolute;top:239px;width:98px;height:99px;background:var(--badge);
    border:3px solid var(--white);outline:3px solid var(--badge);border-radius:4px;
    color:var(--white);text-align:center;font-family:"Open Sans",sans-serif;
  }
  .badge-stain{left:863px}
  .badge-life{left:975px}
  .badge-years{position:absolute;left:8px;top:2px;font:700 52px/60px "Open Sans",sans-serif;letter-spacing:-2px}
  .badge-years small{font:400 7px/1 "Open Sans",sans-serif;letter-spacing:0;margin-left:2px}
  .badge-title{position:absolute;left:0;right:0;top:62px;font-size:10px}
  .badge-note{position:absolute;left:0;right:0;top:82px;font-size:5.6px;white-space:nowrap}
  .badge-ribbon{position:absolute;left:-3px;right:-3px;top:30px;height:26px;background:var(--white);color:#555;font:400 19px/26px "Open Sans",sans-serif}
  .badge-life .badge-title{top:63px}
</style>
</head>
<body>
<main class="poster">
  <div class="deck-photo" role="img" aria-label="Close-up of brown composite deck boards"></div>

  <svg class="header-curve" viewBox="0 0 1095 130" aria-hidden="true">
    <path d="M0,0 H1095 V9 H600 C500,9 455,40 420,72 C385,104 330,112 210,112 H0 Z" fill="var(--band-grey)"/>
    <path d="M0,0 H1095 V6 H560 C470,6 432,36 400,66 C370,94 320,100 200,100 H0 Z" fill="var(--white)"/>
  </svg>

  <div class="brand">
    <span class="brand-mark"></span>
    <span class="brand-name">Brimlay Composites</span>
  </div>
  <div class="website">brimlaydecking.com.au</div>

  <div class="inset-frame">
    <div class="inset-photo" role="img" aria-label="Covered outdoor deck with timber wall, barbecue and wicker lounge"></div>
  </div>

  <h1 class="headline">INDUSTRY’S BEST DECKING<br>WITH BEST WARRANTY</h1>

  <div class="feature-icon icon-maintenance">
    <svg viewBox="0 0 52 52" aria-hidden="true" fill="var(--brand-blue)">
      <rect x="13" y="4" width="20" height="8" rx="1"/>
      <rect x="22" y="10" width="7" height="12"/>
      <path d="M4,22 h10 a7,7 0 0 1 12,0 a7,7 0 0 1 12,0 h10 v7 h-10 a7,7 0 0 1 -12,0 a7,7 0 0 1 -12,0 h-10 Z"/>
      <rect x="22" y="30" width="7" height="6"/>
      <path d="M16,36 h19 l-9.5,11 Z"/>
    </svg>
  </div>
  <div class="feature-icon icon-eco">
    <svg viewBox="0 0 52 52" aria-hidden="true" fill="none" stroke="var(--brand-blue)" stroke-width="3">
      <path d="M8,26 a18,18 0 0 1 30,-13"/>
      <path d="M44,26 a18,18 0 0 1 -30,13"/>
      <path d="M38,7 v7 h-7"/>
      <path d="M14,45 v-7 h7"/>
      <path d="M26,12 C36,20 36,34 26,40 C16,34 16,20 26,12 Z" fill="var(--brand-blue)" stroke="none"/>
      <path d="M26,22 V40 M26,30 l5,-4" stroke="var(--white)" stroke-width="2"/>
    </svg>
  </div>

  <p class="feature-label label-maintenance">ULTRA-LOW<br>MAINTENANCE</p>
  <span class="divider"></span>
  <p class="feature-label label-eco">ENVIRONMENTALLY FRIENDLY<br>Made from Recycled Materials</p>

  <div class="phone-bar"></div>
  <div class="phone-icon">
    <svg width="22" height="22" viewBox="0 0 24 24" aria-hidden="true"><path fill="var(--bar-dark)" d="M6.6 10.8a15.1 15.1 0 0 0 6.6 6.6l2.2-2.2a1 1 0 0 1 1-.25 11.4 11.4 0 0 0 3.6.57 1 1 0 0 1 1 1V20a1 1 0 0 1-1 1A17 17 0 0 1 3 4a1 1 0 0 1 1-1h3.5a1 1 0 0 1 1 1c0 1.25.2 2.450.57 3.57a1 1 0 0 1-.25 1z"/></svg>
  </div>
  <div class="phone-number">1300 947 325</div>

  <div class="badge badge-stain">
    <div class="badge-years">50<small>Year</small></div>
    <div class="badge-title">Stain and Fade</div>
    <div class="badge-note">Limited Residential Warranty</div>
  </div>
  <div class="badge badge-life">
    <div class="badge-ribbon">Lifetime</div>
    <div class="badge-title">Performance</div>
    <div class="badge-note">Limited Residential Warranty</div>
  </div>
</main>
</body>
</html>
```